Awesome Business Card Design needed!

Hey there.
I'm looking for a simple but awesome business card design.
Type of company: Online advertisement agency
(please don't use the typical business people or statistics images on the card)
The front has to display the business name
and possibly some sort of logo ( perhaps something with the two M's of the biz name )
And the back of the card should say:
Name
Phone
Email
Let your imagination flow.
here are some designs that I like and that you can use as inspiration.
Simple but Awesome
http://images.pixelvane.example/designs/55128_877673_43091_thumbnail.jpg
http://images.pixelvane.example/designs/37714_747642_40106_image.jpg
http://images.pixelvane.example/designs/55128_877673_43091_image.jpg
http://images.pixelvane.example/designs/51321_781878_43091_image.jpg
http://images.pixelvane.example/designs/33378_399063_15912_image.jpg
http://images.pixelvane.example/designs/2337_271604_9495_image.jpg
good luck

```html
<!DOCTYPE html>
<html lang="en">
<head>
<meta charset="utf-8">
<title>Tallow Media – Business Card</title>
<link rel="stylesheet" href="https://fonts.googleapis.com/css2?family=Jost:wght@400;600&family=Share+Tech+Mono&display=swap">
<style>
  :root {
    --navy: #00126a;
    --white: #ffffff;
    --frame: #111111;
  }
  html, body {
    margin: 0;
    padding: 0;
    width: 1200px;
    height: 1046px;
    overflow: hidden;
    background: var(--white);
  }
  .sheet {
    position: relative;
    width: 1200px;
    height: 1046px;
  }
  .card {
    position: absolute;
    top: 0;
    height: 1044px;
    box-sizing: border-box;
    overflow: hidden;
  }
  .card--front {
    left: 0;
    width: 580px;
    background: var(--navy);
  }
  .card--back {
    left: 618px;
    width: 581px;
    background: var(--white);
    border: 2px solid var(--frame);
  }
  .brand-name {
    position: absolute;
    left: 0;
    right: 0;
    top: 282px;
    margin: 0;
    text-align: center;
    font-family: "Jost", sans-serif;
    font-weight: 400;
    font-size: 78px;
    line-height: 1;
    color: var(--white);
    white-space: nowrap;
  }
  .contact {
    position: absolute;
    left: 0;
    right: 0;
    margin: 0;
    text-align: center;
    font-family: "Jost", sans-serif;
    color: var(--navy);
    line-height: 1;
    white-space: nowrap;
  }
  .contact__name {
    top: 180px;
    font-weight: 600;
    font-size: 62px;
  }
  .contact__phone {
    top: 336px;
    font-weight: 400;
    font-size: 52px;
  }
  .contact__email {
    top: 466px;
    font-weight: 400;
    font-size: 52px;
    line-height: 62px;
  }
  .tagline {
    position: absolute;
    left: 0;
    right: 0;
    bottom: 14px;
    margin: 0;
    padding-left: 12px;
    text-align: center;
    font-family: "Share Tech Mono", monospace;
    font-size: 30px;
    letter-spacing: 12px;
    line-height: 1;
    white-space: nowrap;
  }
  .card--front .tagline { color: var(--white); }
  .card--back .tagline { color: var(--navy); font-weight: 700; }
</style>
</head>
<body>
  <main class="sheet">
    <section class="card card--front" aria-label="Card front">
      <h1 class="brand-name">Tallow Media</h1>
      <p class="tagline">WE LOVE ADVERTISING</p>
    </section>
    <section class="card card--back" aria-label="Card back">
      <h2 class="contact contact__name">John Doe</h2>
      <p class="contact contact__phone">+123 4556 7899</p>
      <p class="contact contact__email">mail@tallow<br>media.com</p>
      <p class="tagline">WE LOVE ADVERTISING</p>
    </section>
  </main>
</body>
</html>
```